Vorimelo Mobile App

We are in need of a design for a mobile application that delivers relevant content to users based on the profile that they enter and based on the answers that they enter in a daily health tracker. There also will be functionality that will allow a user to check the cost of a medical service/ procedure before going to the medical provider (could get a list of providers and costs after entering procedure, service or prescription in a search box). The content will be articles or information that our team will find/develop on a daily basis and put into a database that the app will pull off of. The profile needs to capture age, sex, ethinicity (optional) and then have a list of topics that the user can select to get daily updated information/content. These topics are: Diabetes, Heart Disease, Hypertension, COPD, Back Pain, Weight Management, Depression, Cancer, Wellness Plan. The final design should allow for users to receive helpful health care information every day based on their profile and the answers in the daily health tracker.

Medical

```html
<!DOCTYPE html>
<html lang="en">
<head>
<meta charset="utf-8">
<title>Vorimelo – Daily Health Tracker</title>
<link rel="stylesheet" href="https://fonts.googleapis.com/css2?family=Arvo:wght@400;700&family=Roboto:wght@300;400&display=swap">
<style>
  :root {
    --page-bg: #dfe9d3;
    --nav-bg: #f3f6ee;
    --field-green: #7bc043;
    --banner-green: #6ca33a;
    --rule-green: #6aab36;
    --question-ink: #2f5a18;
    --banner-ink: #2b4f14;
    --white: #ffffff;
    --brand-blue: #3aa8d8;
    --button-top: #46bde5;
    --button-bottom: #2c9dcf;
    --button-edge: #2589b8;
    --status-ink: #222222;
  }
  * { box-sizing: border-box; margin: 0; padding: 0; }
  html, body {
    width: 1024px; height: 1200px; overflow: hidden;
    background: var(--page-bg);
  }
  .app-screen {
    position: absolute; left: 192px; top: 40px;
    width: 640px; height: 1120px;
    background: var(--field-green);
    overflow: hidden;
    box-shadow: 0 6px 24px rgba(40, 70, 20, 0.18);
  }

  /* Status bar */
  .status-bar {
    height: 40px; background: var(--nav-bg);
    display: flex; align-items: center; justify-content: space-between;
    padding: 0 14px;
    font-family: "Roboto", sans-serif; font-size: 22px; color: var(--status-ink);
  }
  .status-left, .status-right { display: flex; align-items: center; gap: 8px; width: 200px; }
  .status-right { justify-content: flex-end; }
  .signal-dots { display: flex; gap: 3px; }
  .signal-dots span { width: 10px; height: 10px; border-radius: 50%; background: var(--status-ink); }
  .status-time { font-size: 23px; }

  /* Navigation */
  .nav-bar {
    height: 84px; background: var(--nav-bg);
    position: relative; display: flex; align-items: center; justify-content: center;
  }
  .back-button {
    position: absolute; left: 22px; top: 16px;
    height: 52px; width: 100px;
    font-family: "Arvo", serif; font-size: 24px; color: var(--brand-blue);
  }
  .back-button svg { position: absolute; inset: 0; }
  .back-button span { position: absolute; left: 30px; top: 12px; }
  .brand { display: flex; align-items: center; gap: 10px; }
  .brand-dot { width: 18px; height: 18px; border-radius: 50%; background: var(--brand-blue); }
  .brand-name {
    font-family: "Arvo", serif; font-weight: 700; font-size: 27px; color: var(--brand-blue);
  }

  /* Intro banner */
  .intro-banner {
    height: 76px; background: var(--banner-green);
    padding: 13px 32px 0 32px;
    font-family: "Roboto", sans-serif; font-weight: 300; font-size: 17.5px; line-height: 26px;
    color: var(--white);
  }
  .intro-banner strong {
    font-family: "Arvo", serif; font-weight: 700; color: var(--banner-ink); font-size: 17px;
  }

  /* Questions */
  .tracker-question {
    height: 110px; border-bottom: 2px solid var(--rule-green);
    padding: 20px 32px 0 32px;
  }
  .question-text {
    font-family: "Arvo", serif; font-size: 18px; letter-spacing: -0.2px;
    color: var(--question-ink); white-space: nowrap;
    height: 24px; line-height: 24px;
    margin-bottom: 16px;
  }
  .answer-row { display: flex; align-items: center; height: 36px; }
  .answer-row.two-choices .answer { width: 288px; }
  .answer-row.three-choices .answer:nth-child(1) { width: 190px; }
  .answer-row.three-choices .answer:nth-child(2) { width: 176px; }
  .answer {
    display: flex; align-items: center; gap: 14px;
    font-family: "Roboto", sans-serif; font-size: 18.5px; color: var(--white);
    white-space: nowrap;
  }
  .radio {
    width: 34px; height: 34px; border-radius: 50%;
    border: 3px solid var(--white); position: relative; flex: none;
  }
  .radio.is-selected::after {
    content: ""; position: absolute; left: 50%; top: 50%;
    width: 12px; height: 12px; margin: -6px 0 0 -6px;
    border-radius: 50%; background: var(--white);
  }
  .result-entry {
    display: flex; align-items: center; gap: 14px; margin-top: -6px;
    font-family: "Roboto", sans-serif; font-size: 18px; color: var(--white);
  }
  .result-field {
    width: 206px; height: 48px; background: var(--white);
    padding: 12px 14px; font-size: 18px; color: var(--question-ink);
  }

  /* Submit */
  .submit-area { padding: 32px 22px 0 22px; }
  .submit-button {
    width: 100%; height: 104px; border-radius: 8px;
    background: linear-gradient(var(--button-top), var(--button-bottom));
    border: 2px solid var(--button-edge);
    display: flex; align-items: center; justify-content: center;
    font-family: "Arvo", serif; font-size: 36px; color: var(--white);
    text-shadow: 0 1px 1px rgba(0, 60, 90, 0.3);
  }
</style>
</head>
<body>
<main class="app-screen">
  <header class="status-bar">
    <div class="status-left">
      <div class="signal-dots"><span></span><span></span><span></span><span></span><span></span></div>
      <span>Telvia</span>
      <svg width="24" height="18" viewBox="0 0 24 18" aria-hidden="true">
        <path d="M2 6a14 14 0 0 1 20 0M5.5 9.5a9 9 0 0 1 13 0M9 13a4 4 0 0 1 6 0" fill="none" stroke="#222" stroke-width="2.4" stroke-linecap="round"/>
        <circle cx="12" cy="16" r="1.8" fill="#222"/>
      </svg>
    </div>
    <span class="status-time">9:23 AM</span>
    <div class="status-right">
      <svg width="20" height="20" viewBox="0 0 20 20" aria-hidden="true"><path d="M18 2 2 9l7 2 2 7z" fill="#222"/></svg>
      <span>66%</span>
      <svg width="48" height="22" viewBox="0 0 48 22" aria-hidden="true">
        <rect x="1" y="2" width="42" height="18" rx="3" fill="none" stroke="#222" stroke-width="2"/>
        <rect x="4" y="5" width="25" height="12" rx="1" fill="#222"/>
        <rect x="44" y="8" width="3" height="6" rx="1" fill="#222"/>
      </svg>
    </div>
  </header>

  <nav class="nav-bar">
    <div class="back-button">
      <svg width="100" height="52" viewBox="0 0 100 52" aria-hidden="true">
        <path d="M18 2H94a4 4 0 0 1 4 4v40a4 4 0 0 1-4 4H18L2 26z" fill="none" stroke="#3aa8d8" stroke-width="2"/>
      </svg>
      <span>Back</span>
    </div>
    <div class="brand">
      <span class="brand-dot"></span>
      <span class="brand-name">Vorimelo</span>
    </div>
  </nav>

  <section class="intro-banner">
    <strong>Health Care Connected.</strong> This is your personal health tracker. Keep a record of your healthy behaviors and access the history anytime.
  </section>

  <form class="tracker-form">
    <div class="tracker-question">
      <p class="question-text">How many hours did you sleep last night?</p>
      <div class="answer-row two-choices">
        <div class="answer"><span class="radio is-selected"></span>Less than 6 hours</div>
        <div class="answer"><span class="radio"></span>More than 6 hours</div>
      </div>
    </div>
    <div class="tracker-question">
      <p class="question-text">Have you exercised today?</p>
      <div class="answer-row two-choices">
        <div class="answer"><span class="radio is-selected"></span>Yes</div>
        <div class="answer"><span class="radio"></span>No</div>
      </div>
    </div>
    <div class="tracker-question">
      <p class="question-text">Have you had a cigarette today?</p>
      <div class="answer-row two-choices">
        <div class="answer"><span class="radio is-selected"></span>Yes</div>
        <div class="answer"><span class="radio"></span>No</div>
      </div>
    </div>
    <div class="tracker-question">
      <p class="question-text">Have you had any alcoholic beverages today?</p>
      <div class="answer-row two-choices">
        <div class="answer"><span class="radio is-selected"></span>Yes</div>
        <div class="answer"><span class="radio"></span>No</div>
      </div>
    </div>
    <div class="tracker-question">
      <p class="question-text">How would you describe your eating over the last 24 hrs?</p>
      <div class="answer-row three-choices">
        <div class="answer"><span class="radio is-selected"></span>Healthy</div>
        <div class="answer"><span class="radio"></span>Not bad</div>
        <div class="answer"><span class="radio"></span>Needs improvement</div>
      </div>
    </div>
    <div class="tracker-question">
      <p class="question-text">How would you describe your stress level over the last 24 hrs?</p>
      <div class="answer-row three-choices">
        <div class="answer"><span class="radio is-selected"></span>Healthy</div>
        <div class="answer"><span class="radio"></span>Not bad</div>
        <div class="answer"><span class="radio"></span>Needs improvement</div>
      </div>
    </div>
    <div class="tracker-question">
      <p class="question-text">Have you checked your insulin levels today?</p>
      <div class="result-entry">
        <span>If yes, enter results here:</span>
        <div class="result-field">#</div>
      </div>
    </div>

    <div class="submit-area">
      <div class="submit-button">Submit to your Health Tracker</div>
    </div>
  </form>
</main>
</body>
</html>
```